Redgum Party Box and Bouncer Hire

Hi folks,
This is for a new business based in Brisbane(Australia), the business hires, jukeboxes, inflatable games(mostly jumping castles) and slushy/cocktail machines.
I want the website to appeal to people looking to party. Does that sound too simplistic?
It should be simple to navigate, I require only the front page but make it easy to get to the rest of the site.
Modern, exciting and funky, think rock band or concert promoter.
We are trying to sell packages of products, there should be several packages visible on the front page without looking cluttered.
Link to jukebox song list.
Facebook, twitter etc.
I am currently on holidays so I have a fair amount of time to get this project done, it says 10 days I hope to have it done much sooner.

Reason: So far there is no design that I am happy with. I am after a website for Jukeboxes, it should have a rock concert feel.

Target Market(s)

Ages 20 to 50

Industry/Entity Type

Business

Requirements
Must have
• Think rock band type website, black with bold color highlight.
Should not have
• Plain or bland color.
Pictures of Brisbane or any other city.
Google map or any other location type map.

```html
<!DOCTYPE html>
<html lang="en">
<head>
<meta charset="utf-8">
<title>Redgum Party Box and Bouncer Hire</title>
<link href="https://fonts.googleapis.com/css2?family=Arimo:ital,wght@0,400;0,700;1,400&display=swap" rel="stylesheet">
<style>
:root{
  --pink:#e8185f;
  --blue:#1187c6;
  --cyan:#0bb5c9;
  --olive:#a3ad02;
  --olive-dark:#8e9700;
  --olive-line:#b4bd2a;
  --grey-band:#dcdcdc;
  --footer:#4a4a4a;
  --text:#6b6b6b;
  --white:#fff;
}
*{margin:0;padding:0;box-sizing:border-box}
html,body{width:674px;height:1200px;overflow:hidden}
body{position:relative;background:var(--white);font-family:"Arimo",Arial,sans-serif;color:var(--text)}
.abs{position:absolute}
.top-band{left:0;top:0;width:674px;height:298px;background:var(--grey-band)}
.header{left:96px;top:0;width:482px;height:46px;background:var(--white)}
.logo{left:14px;top:15px;font-size:14px;font-weight:700;color:var(--pink);white-space:nowrap}
.social{right:14px;top:15px;display:flex;gap:5px}
.social span{width:16px;height:16px;border-radius:50%;background:#3fa6dc;display:block}
.nav{left:96px;top:46px;width:482px;height:22px;background:var(--pink);display:flex}
.nav a{flex:1;color:var(--white);font-size:6.5px;text-decoration:none;display:flex;align-items:center;justify-content:center;border-right:1px solid #f0578d}
.nav a:last-child{border-right:none}
.hero{left:96px;top:73px;width:482px;height:200px;background:linear-gradient(180deg,#0d1a3a 0%,#1c2d5a 55%,#3a3a40 80%,#1a1f2e 100%)}
.hero-title{left:413px;top:130px;color:var(--white);font-size:17px;line-height:21px;font-weight:400;white-space:nowrap}
.hero-text{left:413px;top:176px;color:var(--white);font-size:6.8px;line-height:14px;width:155px}
.hero-arrows{left:543px;top:250px;display:flex;gap:2px}
.hero-arrows span{width:12px;height:12px;background:var(--pink);color:var(--white);font-size:9px;line-height:11px;text-align:center}
.welcome-img{left:96px;top:329px;width:149px;height:108px;background:linear-gradient(135deg,#8fd14f,#5cae2e 60%,#d7d23a)}
.section-title{color:var(--blue);font-size:10px;font-weight:400}
.body-text{font-size:5.3px;line-height:11.6px}
.welcome-body{left:261px;top:346px;width:306px}
.card{width:108px}
.card-img{width:108px;height:79px}
.card-head{color:var(--pink);font-size:5.8px;line-height:11.6px;margin-top:13px}
.ticks{list-style:none;margin-top:7px}
.ticks li{font-size:5.3px;height:14px;display:flex;align-items:center;gap:4px}
.price{color:var(--pink);font-size:14px;text-align:center;margin-top:8px}
.btn{display:block;margin-top:7px;height:20px;background:var(--cyan);color:var(--white);font-size:5.8px;font-weight:700;text-align:center;line-height:20px}
.green-band{left:0;top:721px;width:674px;height:228px;background:var(--olive)}
.green-title{color:var(--white);font-size:9.5px;font-weight:400}
.news-img{width:86px;height:63px}
.news-head{color:var(--white);font-size:7px}
.news-date{color:var(--white);font-size:5.5px;font-style:italic;margin-top:7px}
.news-body{color:var(--white);font-size:5.3px;line-height:11.6px;margin-top:8px;width:172px}
.songs{left:396px;top:768px;width:181px}
.songs li{list-style:none;height:21.4px;background:var(--olive-dark);border-bottom:1px solid var(--olive-line);display:flex;align-items:center;color:var(--white);font-size:5.3px}
.songs li i{width:20px;height:100%;border-right:1px solid var(--olive-line);display:flex;align-items:center;justify-content:center;font-style:normal;font-size:7px;margin-right:4px}
.testi-title{left:0;top:975px;width:674px;text-align:center;color:var(--blue);font-size:10px;font-weight:400}
.testi-intro{left:100px;top:999px;width:474px;text-align:center;font-size:5.3px;line-height:13.5px}
.divider{left:218px;top:1037px;width:238px;height:1px;background:#e2e2e2}
.divider-dot{left:333px;top:1035px;width:5px;height:5px;border:1px solid #ccc;border-radius:50%;background:var(--white)}
.avatar{width:62px;height:62px;border-radius:50%}
.t-name{color:var(--pink);font-size:7px}
.t-date{font-size:4.8px;font-style:italic;margin-top:6px}
.t-body{font-size:5.5px;line-height:12px;margin-top:5px;width:136px}
.t-arrow{color:#c8c8c8;font-size:14px}
.footer{left:0;top:1142px;width:674px;height:58px;background:var(--footer)}
.foot-links{left:0;top:17px;width:674px;text-align:center;color:#ddd;font-size:5.3px;word-spacing:2px}
.copy{left:0;top:35px;width:674px;text-align:center;color:#ddd;font-size:5.3px}
</style>
</head>
<body>
<div class="abs top-band"></div>

<header class="abs header">
  <div class="abs logo">Redgum Party Box and Bouncer Hire</div>
  <div class="abs social" aria-label="Social links">
    <span></span><span></span><span></span><span></span><span></span>
  </div>
</header>

<nav class="abs nav">
  <a>Home</a><a>About Us</a><a>Services</a><a>Packages</a><a>Gallery</a><a>Jukebox songs</a><a>Testimonials</a><a>Contact us</a>
</nav>

<section>
  <div class="abs hero" role="img" aria-label="Night photograph of a lit bridge over a harbour"></div>
  <h1 class="abs hero-title">Redgum Party Box<br>&amp; Bouncer Hire</h1>
  <p class="abs hero-text">We give jukeboxes, inflatable games and jumping castles, cocktail machines etc..</p>
  <div class="abs hero-arrows"><span>&#8249;</span><span>&#8250;</span></div>
</section>

<section>
  <div class="abs welcome-img" role="img" aria-label="Child laughing in a ball pit"></div>
  <h2 class="abs section-title" style="left:261px;top:329px">Welcome to Redgum Party Box and Bouncer Hire</h2>
  <div class="abs body-text welcome-body">
    <p>Lorem ipsum is simply dummy text of the printing and typesetting industry. Lorem ipsum has been the industry's standard dummy text ever since the 1500s, when an unknown printer took a galley of type and scrambled it to make a type specimen book. It has survived not only five centuries, but also the leap into electronic typesetting, remaining essentially unchanged. It was popularised in the 1960s with the release of sheets containing lorem ipsum passages, and more recently with desktop publishing and layout software including versions of lorem ipsum.</p>
    <p style="margin-top:11.6px">Remaining essentially unchanged. It was popularised in the 1960s with the release of sheets containing lorem ipsum passages, and more recently with desktop publishing...</p>
  </div>
</section>

<section>
  <h2 class="abs section-title" style="left:96px;top:462px">Packages of products</h2>

  <div class="abs card" style="left:96px;top:486px">
    <div class="card-img" role="img" aria-label="Colourful inflatable jumping castle" style="background:linear-gradient(135deg,#f2c21b,#e53a2f 50%,#2e7ad6)"></div>
    <p class="card-head">Lorem Ipsum is simply dummy text of the printing and typesetting...</p>
    <ul class="ticks">
      <li><svg width="8" height="7" viewBox="0 0 8 7"><path d="M1 3.5 3 5.5 7 1" fill="none" stroke="#8cbf26" stroke-width="1.5"/></svg>Lorem Ipsum is simply dummy.</li>
      <li><svg width="8" height="7" viewBox="0 0 8 7"><path d="M1 3.5 3 5.5 7 1" fill="none" stroke="#8cbf26" stroke-width="1.5"/></svg>Lorem Ipsum is simply dummy.</li>
      <li><svg width="8" height="7" viewBox="0 0 8 7"><path d="M1 3.5 3 5.5 7 1" fill="none" stroke="#8cbf26" stroke-width="1.5"/></svg>Lorem Ipsum is simply dummy.</li>
    </ul>
    <p class="price">$60.00</p>
    <a class="btn">SELECT YOUR PACKAGE</a>
  </div>

  <div class="abs card" style="left:220px;top:486px">
    <div class="card-img" role="img" aria-label="Children playing on an inflatable slide" style="background:linear-gradient(160deg,#f4e04a,#3cc7b0 55%,#1ea88f)"></div>
    <p class="card-head">Lorem Ipsum is simply dummy text of the printing and typesetting...</p>
    <ul class="ticks">
      <li><svg width="8" height="7" viewBox="0 0 8 7"><path d="M1 3.5 3 5.5 7 1" fill="none" stroke="#8cbf26" stroke-width="1.5"/></svg>Lorem Ipsum is simply dummy.</li>
      <li><svg width="8" height="7" viewBox="0 0 8 7"><path d="M1 3.5 3 5.5 7 1" fill="none" stroke="#8cbf26" stroke-width="1.5"/></svg>Lorem Ipsum is simply dummy.</li>
      <li><svg width="8" height="7" viewBox="0 0 8 7"><path d="M1 3.5 3 5.5 7 1" fill="none" stroke="#8cbf26" stroke-width="1.5"/></svg>Lorem Ipsum is simply dummy.</li>
    </ul>
    <p class="price">$60.00</p>
    <a class="btn">SELECT YOUR PACKAGE</a>
  </div>

  <div class="abs card" style="left:346px;top:486px">
    <div class="card-img" role="img" aria-label="Inflatable climbing wall" style="background:linear-gradient(120deg,#2f6fd0,#e3502a 55%,#f4a321)"></div>
    <p class="card-head">Lorem Ipsum is simply dummy text of the printing and typesetting...</p>
    <ul class="ticks">
      <li><svg width="8" height="7" viewBox="0 0 8 7"><path d="M1 3.5 3 5.5 7 1" fill="none" stroke="#8cbf26" stroke-width="1.5"/></svg>Lorem Ipsum is simply dummy.</li>
      <li><svg width="8" height="7" viewBox="0 0 8 7"><path d="M1 3.5 3 5.5 7 1" fill="none" stroke="#8cbf26" stroke-width="1.5"/></svg>Lorem Ipsum is simply dummy.</li>
      <li><svg width="8" height="7" viewBox="0 0 8 7"><path d="M1 3.5 3 5.5 7 1" fill="none" stroke="#8cbf26" stroke-width="1.5"/></svg>Lorem Ipsum is simply dummy.</li>
    </ul>
    <p class="price">$60.00</p>
    <a class="btn">SELECT YOUR PACKAGE</a>
  </div>

  <div class="abs card" style="left:470px;top:486px">
    <div class="card-img" role="img" aria-label="Row of colourful cocktails on a dark background" style="background:linear-gradient(180deg,#222 0%,#111 40%,#4a8a2a 60%,#c23a5a 80%,#0a0a0a)"></div>
    <p class="card-head">Lorem Ipsum is simply dummy text of the printing and typesetting...</p>
    <ul class="ticks">
      <li><svg width="8" height="7" viewBox="0 0 8 7"><path d="M1 3.5 3 5.5 7 1" fill="none" stroke="#8cbf26" stroke-width="1.5"/></svg>Lorem Ipsum is simply dummy.</li>
      <li><svg width="8" height="7" viewBox="0 0 8 7"><path d="M1 3.5 3 5.5 7 1" fill="none" stroke="#8cbf26" stroke-width="1.5"/></svg>Lorem Ipsum is simply dummy.</li>
      <li><svg width="8" height="7" viewBox="0 0 8 7"><path d="M1 3.5 3 5.5 7 1" fill="none" stroke="#8cbf26" stroke-width="1.5"/></svg>Lorem Ipsum is simply dummy.</li>
    </ul>
    <p class="price">$60.00</p>
    <a class="btn">SELECT YOUR PACKAGE</a>
  </div>
</section>

<section class="abs green-band"></section>
<h2 class="abs green-title" style="left:96px;top:741px">News &amp; Events</h2>

<div class="abs news-img" role="img" aria-label="Toddler playing in an inflatable pool" style="left:96px;top:765px;background:linear-gradient(135deg,#f5d640,#e9a24a 60%,#d9532c)"></div>
<div class="abs" style="left:192px;top:765px">
  <p class="news-head">Lorem Ipsum is simply dummy text of the printing :</p>
  <p class="news-date">Posted on 27 March 2014</p>
  <p class="news-body">Lorem Ipsum is simply dummy text of the printing and typesetting industry. Lorem Ipsum has been the industry's standard dummy text ever since the 1500s</p>
</div>

<div class="abs news-img" role="img" aria-label="Child on a blue inflatable water slide" style="left:96px;top:853px;background:linear-gradient(120deg,#1f4fb8,#f1f3f7 60%,#b9d0e6)"></div>
<div class="abs" style="left:192px;top:853px">
  <p class="news-head">Lorem Ipsum is simply dummy text of the printing :</p>
  <p class="news-date">Posted on 27 March 2014</p>
  <p class="news-body">Lorem Ipsum is simply dummy text of the printing and typesetting industry. Lorem Ipsum has been the industry's standard dummy text ever since the 1500s</p>
</div>

<h2 class="abs green-title" style="left:398px;top:744px">Jukebox songs</h2>
<ul class="abs songs">
  <li><i>&#8250;</i>Lorem Ipsum is simply dummy text of the printing</li>
  <li><i>&#8250;</i>Lorem Ipsum is simply dummy text of printing</li>
  <li><i>&#8250;</i>Lorem Ipsum is simply dummy text</li>
  <li><i>&#8250;</i>Lorem Ipsum is simply dummy text of the printing</li>
  <li><i>&#8250;</i>Lorem Ipsum is simply dummy</li>
  <li><i>&#8250;</i>Lorem Ipsum is simply dummy printing</li>
  <li><i>&#8250;</i>Lorem Ipsum is simply dummy text of the printing</li>
</ul>

<section>
  <h2 class="abs testi-title">Testimonials</h2>
  <p class="abs testi-intro">It is a long established fact that a reader will be distracted by the readable content of a page when looking at its layout. The point of using Lorem Ipsum is that it has a more-or-less normal distribution of letters, as opposed to using 'Content here, content here...</p>
  <div class="abs divider"></div>
  <div class="abs divider-dot"></div>

  <span class="abs t-arrow" style="left:88px;top:1070px">&#8249;</span>
  <span class="abs t-arrow" style="left:584px;top:1070px">&#8250;</span>

  <div class="abs avatar" role="img" aria-label="Portrait of a smiling family" style="left:114px;top:1048px;background:radial-gradient(circle at 45% 45%,#f0c7a3,#5fa6d8 75%)"></div>
  <div class="abs" style="left:192px;top:1056px">
    <p class="t-name">Marla Quinn</p>
    <p class="t-date">Posted on 27 march 2014</p>
    <p class="t-body">It is a long established fact that a reader will be distracted by the readable content...</p>
  </div>

  <div class="abs avatar" role="img" aria-label="Portrait of a smiling family" style="left:354px;top:1048px;background:radial-gradient(circle at 50% 45%,#f1cfae,#e9eef3 75%)"></div>
  <div class="abs" style="left:433px;top:1056px">
    <p class="t-name">Marla Quinn</p>
    <p class="t-date">Posted on 27 march 2014</p>
    <p class="t-body">It is a long established fact that a reader will be distracted by the readable content...</p>
  </div>
</section>

<footer class="abs footer">
  <p class="abs foot-links">Home &nbsp;|&nbsp; About Us &nbsp;|&nbsp; Services &nbsp;|&nbsp; Packages &nbsp;|&nbsp; Gallery &nbsp;|&nbsp; Jukebox songs &nbsp;|&nbsp; Testimonials &nbsp;|&nbsp; Contact us</p>
  <p class="abs copy">Copyright 2014. Redgum Party Box and Bouncer Hire. All rights reserved.</p>
</footer>
</body>
</html>
```